Automotive Business Card Design

I would just like a automotive themed card. nothing too extravagant, but catchy.

needs to say something about doing roadside assistance,mobile repairs, Diesel repairs, and Fleet maintenance

it can be single sided or double sided. no preference there.

Industry/Entity Type

Automotive

Contact Information for Business Card

Dean Marwick
phone 519 374 2083
Name: Brightway Automotive & Diesel Repair

```html
<!DOCTYPE html>
<html lang="en">
<head>
<meta charset="UTF-8">
<title>Brightway Automotive &amp; Diesel Repair — Business Card</title>
<link rel="stylesheet" href="https://fonts.googleapis.com/css2?family=Cinzel:wght@400;500&family=Jost:wght@400;600&display=swap">
<style>
  :root {
    --page-bg: #2a2a2a;
    --card-top: #ffffff;
    --card-bottom: #e4e4e4;
    --ink: #1a1a1a;
    --ink-soft: #333333;
    --accent-red: #c4151c;
    --car-light: #f2f2f2;
    --car-mid: #c9c9c9;
    --car-dark: #8a8a8a;
  }
  * { box-sizing: border-box; margin: 0; padding: 0; }
  html, body {
    width: 1200px;
    height: 900px;
    overflow: hidden;
  }
  body {
    background: var(--page-bg);
    position: relative;
    font-family: "Jost", sans-serif;
    color: var(--ink);
  }
  .business-card {
    position: absolute;
    left: 100px;
    top: 164px;
    width: 1000px;
    height: 572px;
    border-radius: 36px;
    background: linear-gradient(160deg, var(--card-top) 0%, #f6f6f6 55%, var(--card-bottom) 100%);
    overflow: hidden;
  }
  .company-name {
    position: absolute;
    left: 58px;
    top: 46px;
    font-family: "Cinzel", serif;
    font-weight: 500;
    font-size: 33px;
    letter-spacing: 2px;
    color: var(--ink);
    white-space: nowrap;
  }
  .car-photo {
    position: absolute;
    right: 0;
    top: 96px;
    width: 470px;
    height: 400px;
    border-radius: 40px 0 0 40px;
    background: radial-gradient(ellipse at 45% 50%, var(--car-light) 0%, var(--car-mid) 55%, var(--car-dark) 100%);
    opacity: 0.9;
  }
  .greeting {
    position: absolute;
    left: 58px;
    top: 200px;
    font-size: 40px;
    font-weight: 400;
    letter-spacing: 1px;
  }
  .owner-name {
    position: absolute;
    left: 58px;
    top: 248px;
    font-size: 46px;
    font-weight: 600;
    color: var(--accent-red);
    letter-spacing: 1px;
    text-transform: uppercase;
  }
  .phone-line {
    position: absolute;
    left: 58px;
    top: 306px;
    display: flex;
    align-items: center;
    gap: 20px;
    font-size: 46px;
    font-weight: 400;
  }
  .phone-icon { width: 46px; height: 40px; }
  .service-list {
    position: absolute;
    left: 58px;
    top: 398px;
    list-style: none;
    font-size: 27px;
    color: var(--ink-soft);
    letter-spacing: 0.5px;
  }
  .service-item {
    position: relative;
    padding-left: 26px;
    line-height: 1.15;
    margin-bottom: 14px;
  }
  .service-item::before {
    content: "";
    position: absolute;
    left: 0;
    top: 4px;
    bottom: 4px;
    width: 6px;
    background: var(--accent-red);
  }
</style>
</head>
<body>
  <section class="business-card">
    <h1 class="company-name">Brightway Automotive &amp; Diesel Repair</h1>

    <div class="car-photo" role="img" aria-label="Photograph of a silver sedan seen from the rear three-quarter view"></div>

    <p class="greeting">Hi, I’M</p>
    <p class="owner-name">Dean Marwick</p>
    <p class="phone-line">
      <svg class="phone-icon" viewBox="0 0 46 40" aria-hidden="true">
        <path d="M2 12 C2 4 44 4 44 12 L44 16 L34 16 L34 11 C28 9 18 9 12 11 L12 16 L2 16 Z" fill="var(--accent-red)"/>
        <path d="M14 16 L32 16 L40 30 L40 38 L6 38 L6 30 Z" fill="var(--accent-red)"/>
        <circle cx="23" cy="28" r="6" fill="#ffffff"/>
        <circle cx="23" cy="28" r="2.5" fill="var(--accent-red)"/>
      </svg>
      <span class="phone-number">519 374 2083</span>
    </p>

    <ul class="service-list">
      <li class="service-item">Roadside Assistance,</li>
      <li class="service-item">Mobile Repairs,</li>
      <li class="service-item">Diesel Repairs<br>&amp; Fleet Maintenance</li>
    </ul>
  </section>
</body>
</html>
```